New Business Cards for Organic Meat Farm

We need a business card designed for Thornbury Farm, a meat farm in western MA. Our logo uses a hand-drawn woodcut (attached). Our color palette has been simply black and white (shown in notepad and picture of our food truck). While we are based out of western MA, we have ambitions to grow nationally, so our hope is for a classy and memorable card which will be printed on a premium quality stock from a printer like printkestrel.com.
Target Market(s)
consumers of quality meats, restauranteurs, partnering farms
Industry/Entity Type
Farming and prepared meat products
Contact Information for Business Card
Wendell Pruitt, President/Owner, wendell@thornburyfarm.com, mobile: 413-555-0172, phone: 413-555-0148, thornburyfarm.com, facebook: @thornburyfarm, instagram: @thornburyfarmma
Colors
Designer to choose colors to be used in the design.
Look and feel

```html
<!DOCTYPE html>
<html lang="en">
<head>
<meta charset="utf-8">
<title>Thornbury Farm – Business Card</title>
<link href="https://fonts.googleapis.com/css2?family=Poppins:wght@400;500;600&display=swap" rel="stylesheet">
<style>
  :root {
    --backdrop: #d3d7d8;
    --card-dark: #222226;
    --card-light: #ffffff;
    --ink: #111111;
    --paper: #ffffff;
    --ghost: #dcdcdc;
    --ghost-soft: #ececec;
    --mark-dark: #3a3a3a;
  }
  * { margin: 0; padding: 0; box-sizing: border-box; }
  html, body {
    width: 1200px; height: 960px; overflow: hidden;
    background: var(--backdrop);
    font-family: "Poppins", sans-serif;
  }
  .canvas { position: relative; width: 1200px; height: 960px; }

  .card { position: absolute; overflow: hidden; }
  .card--front { left: 247px; top: 58px; width: 706px; height: 404px; background: var(--card-dark); }
  .card--back { left: 249px; top: 500px; width: 702px; height: 401px; background: var(--card-light); }

  .house-art { position: absolute; }
  .card--front .house-art {
    left: 208px; top: 74px; width: 288px; height: 118px;
    border-radius: 144px 144px 6px 6px / 90px 90px 6px 6px;
    background: linear-gradient(180deg, #e8e8e8 0%, #9a9a9a 100%);
  }
  .wordmark { position: absolute; text-align: center; font-weight: 600; }
  .wordmark__name { display: block; }
  .wordmark__sub { display: block; letter-spacing: 0.3em; }
  .card--front .wordmark { left: 0; right: 0; top: 208px; color: var(--paper); }
  .card--front .wordmark__name { font-size: 46px; line-height: 1.1; }
  .card--front .wordmark__sub { font-size: 26px; margin-top: 14px; padding-left: 0.3em; }

  .backdrop-art {
    position: absolute; left: 0; top: 0; width: 440px; height: 401px;
    background: linear-gradient(160deg, var(--ghost) 0%, var(--ghost-soft) 70%, rgba(255,255,255,0) 100%);
    border-radius: 0 200px 0 0 / 0 220px 0 0;
  }
  .card--back .house-art {
    left: 533px; top: 25px; width: 143px; height: 60px;
    border-radius: 72px 72px 4px 4px / 44px 44px 4px 4px;
    background: linear-gradient(180deg, #6a6a6a 0%, var(--ink) 100%);
  }
  .card--back .wordmark { left: 530px; width: 150px; top: 88px; color: var(--ink); }
  .card--back .wordmark__name { font-size: 22px; line-height: 1.2; }
  .card--back .wordmark__sub { font-size: 13px; margin-top: 2px; padding-left: 0.3em; }

  .person { position: absolute; right: 27px; top: 168px; text-align: right; color: var(--ink); }
  .person__name { font-size: 30px; font-weight: 600; line-height: 1.2; }
  .person__role { font-size: 15px; font-weight: 500; }
  .accent-bar { position: absolute; right: 0; top: 178px; width: 16px; height: 42px; background: var(--ink); }

  .contact { position: absolute; right: 25px; list-style: none; color: var(--ink); }
  .contact--social { top: 238px; }
  .contact--direct { top: 294px; }
  .contact li {
    display: flex; justify-content: flex-end; align-items: center;
    font-size: 15.5px; line-height: 21px; height: 21px; gap: 10px;
  }
  .contact svg { width: 14px; height: 14px; flex: none; }
</style>
</head>
<body>
<main class="canvas">

  <section class="card card--front" aria-label="Card front">
    <div class="house-art" role="img" aria-label="Woodcut illustration of the farmhouse with trees"></div>
    <div class="wordmark">
      <span class="wordmark__name">Thornbury</span>
      <span class="wordmark__sub">FARM</span>
    </div>
  </section>

  <section class="card card--back" aria-label="Card back">
    <div class="backdrop-art" role="img" aria-label="Faint enlarged woodcut of the farmhouse and trees"></div>
    <div class="house-art" role="img" aria-label="Small woodcut illustration of the farmhouse"></div>
    <div class="wordmark">
      <span class="wordmark__name">Thornbury</span>
      <span class="wordmark__sub">FARM</span>
    </div>

    <div class="person">
      <p class="person__name">Wendell Pruitt</p>
      <p class="person__role">President/Owner</p>
    </div>
    <div class="accent-bar"></div>

    <ul class="contact contact--social">
      <li>@thornburyfarm
        <svg viewBox="0 0 14 14"><circle cx="7" cy="7" r="6.5" fill="#111"/></svg></li>
      <li>@thornburyfarmma
        <svg viewBox="0 0 14 14"><rect x="1" y="1" width="12" height="12" rx="3" fill="none" stroke="#111" stroke-width="1.6"/></svg></li>
    </ul>

    <ul class="contact contact--direct">
      <li>413-555-0172
        <svg viewBox="0 0 14 14"><rect x="3.5" y="0.8" width="7" height="12.4" rx="1.2" fill="none" stroke="#111" stroke-width="1.5"/></svg></li>
      <li>413-555-0148
        <svg viewBox="0 0 14 14"><path d="M3 1.5 L5.2 1.5 L6 4.5 L4.6 5.6 Q5.8 8.3 8.4 9.4 L9.5 8 L12.5 8.8 L12.5 11 Q12 12.8 10 12.5 Q3.5 11 1.5 4 Q1.3 1.8 3 1.5 Z" fill="#111"/></svg></li>
      <li>www.thornburyfarm.com
        <svg viewBox="0 0 14 14"><circle cx="7" cy="7" r="6" fill="none" stroke="#111" stroke-width="1.4"/><ellipse cx="7" cy="7" rx="2.6" ry="6" fill="none" stroke="#111" stroke-width="1.1"/><line x1="1" y1="7" x2="13" y2="7" stroke="#111" stroke-width="1.1"/></svg></li>
      <li>wendell@thornburyfarm.com
        <svg viewBox="0 0 14 14"><rect x="1" y="3" width="12" height="9" fill="none" stroke="#111" stroke-width="1.4"/><path d="M1 3 L7 8 L13 3" fill="none" stroke="#111" stroke-width="1.4"/></svg></li>
    </ul>
  </section>

</main>
</body>
</html>
```